Plakate für eine Veranstaltung
Sehr professionelle Umsetzung, schnelle Absprachen und freundlicher Kontakt. Immer wieder gerne, vielen Dank lieber Karvano.
Zielgruppe
Musikerin / Sängerin, Wir suchen ein hochwertiges Plakat mit unseren Specials Guests für ein Publikum mittleren Alters.
Aufgabenstellung
Anlage in Din1, Titel der Veranstaltung: 'Velvet Lantern Serenade' - Petra Holwig & Friends in concert, hochauflösende Bilder sind fast komplett vorhanden, gerne erst mal mit vorhandenen Material Idee kreieren und im Anschluss austauschen. Details zum Konzert: 16.11.23, Bühnenhaus am Ulmenfeld Lingen, 19.30 Uhr, Veranstalter: Stadt Lingen. Gerne die Hauptsängerin im Fokus und die anderen Aktiven in Einblendung einarbeiten. Name der Special Guest stehen als Dateiname in den angehängten Files.

```html
<!DOCTYPE html>
<html lang="de">
<head>
<meta charset="utf-8">
<title>Petra Holwig &amp; Friends in Concert – Plakat</title>
<link rel="stylesheet" href="https://fonts.googleapis.com/css2?family=Playfair+Display:wght@600;700&family=Figtree:wght@400;500;700&display=swap">
<style>
  :root {
    --page: #ffffff;
    --ink-dark: #232323;
    --brown-deep: #1c130d;
    --brown-mid: #4a3624;
    --gold: #e8bf4a;
    --gold-light: #e6d28e;
    --gold-deep: #a9853f;
    --bokeh-light: #d9b77e;
    --bokeh-dark: #6e5230;
    --white: #ffffff;
  }
  html, body {
    margin: 0;
    width: 1000px;
    height: 1200px;
    overflow: hidden;
    background: var(--page);
  }
  .poster {
    position: absolute;
    left: 90px;
    top: 20px;
    width: 820px;
    height: 1160px;
  }
  .poster svg { display: block; width: 100%; height: 100%; }
  .headline { font-family: "Playfair Display", Georgia, serif; font-weight: 700; fill: var(--white); }
  .event-title { font-family: "Playfair Display", Georgia, serif; font-weight: 600; fill: var(--gold); letter-spacing: 1px; }
  .guest-label { font-family: "Figtree", Arial, sans-serif; font-weight: 400; fill: var(--white); }
  .event-date { font-family: "Figtree", Arial, sans-serif; font-weight: 700; fill: var(--white); }
  .event-venue { font-family: "Figtree", Arial, sans-serif; font-weight: 400; fill: var(--white); }
</style>
</head>
<body>
<main class="poster">
  <svg viewBox="0 0 1052 1488" xmlns="http://www.w3.org/2000/svg">
    <defs>
      <linearGradient id="topBg" x1="0" y1="0" x2="0" y2="1">
        <stop offset="0" stop-color="#2a1d12"/>
        <stop offset="1" stop-color="#5a4430"/>
      </linearGradient>
      <radialGradient id="singerTone" cx="0.45" cy="0.45" r="0.6">
        <stop offset="0" stop-color="#b9774a"/>
        <stop offset="0.55" stop-color="#5e2a22"/>
        <stop offset="1" stop-color="#1a0f0c"/>
      </radialGradient>
      <linearGradient id="goldBand" x1="0" y1="0" x2="1" y2="0">
        <stop offset="0" stop-color="#b08a45"/>
        <stop offset="0.6" stop-color="#e6d28e"/>
        <stop offset="1" stop-color="#c9a45a"/>
      </linearGradient>
      <radialGradient id="bokeh" cx="0.5" cy="0.3" r="0.8">
        <stop offset="0" stop-color="var(--bokeh-light)"/>
        <stop offset="0.7" stop-color="#b38d55"/>
        <stop offset="1" stop-color="var(--bokeh-dark)"/>
      </radialGradient>
      <radialGradient id="violinTone" cx="0.5" cy="0.5" r="0.6">
        <stop offset="0" stop-color="#b0304a"/><stop offset="1" stop-color="#1c0f14"/>
      </radialGradient>
      <radialGradient id="pianistTone" cx="0.5" cy="0.5" r="0.6">
        <stop offset="0" stop-color="#f2f2f2"/><stop offset="1" stop-color="#8c8c8c"/>
      </radialGradient>
      <radialGradient id="pipesTone" cx="0.5" cy="0.5" r="0.6">
        <stop offset="0" stop-color="#3c6a7c"/><stop offset="1" stop-color="#18242c"/>
      </radialGradient>
      <path id="titleArc" d="M90,878 C300,800 560,706 740,700 C880,696 960,730 1030,790"/>
    </defs>

    <!-- top stage backdrop -->
    <rect class="backdrop" width="1052" height="1488" fill="url(#topBg)"/>
    <rect class="choir-photo" x="520" y="150" width="532" height="520" fill="#6b5540" opacity="0.55"
          role="img" aria-label="Chor auf der Bühne, sepiafarben"/>
    <rect class="snowflake-decor" x="660" y="0" width="230" height="130" fill="#7a6a5a" opacity="0.25"
          role="img" aria-label="Schneeflocken-Ornament"/>
    <rect class="filmstrip-decor" x="870" y="0" width="182" height="190" fill="var(--gold)" opacity="0.35"
          role="img" aria-label="Filmstreifen-Ornament"/>

    <!-- lead singer -->
    <path class="singer-photo" d="M0,150 C120,80 330,70 470,150 C580,215 610,360 590,520 L560,740 L0,740 Z"
          fill="url(#singerTone)" role="img" aria-label="Sängerin mit Mikrofon im Bühnenlicht"/>

    <!-- headline -->
    <text class="headline" x="1000" y="292" text-anchor="end" font-size="84">PETRA HOLWIG</text>
    <text class="headline" x="1000" y="382" text-anchor="end" font-size="82">&amp; Friends</text>
    <text class="headline" x="1000" y="474" text-anchor="end" font-size="82">in Concert</text>

    <!-- lower gold area -->
    <rect class="bokeh-field" x="0" y="760" width="1052" height="560" fill="url(#bokeh)"/>

    <!-- gold wave + dark title band -->
    <path class="gold-wave" d="M0,700 C250,780 480,640 700,545 C850,485 970,500 1052,520 L1052,640 C980,600 880,570 720,605 C500,655 250,800 0,742 Z"
          fill="url(#goldBand)"/>
    <path class="title-band" d="M0,742 C250,800 500,655 720,605 C880,570 980,600 1052,640 L1052,915 C930,820 720,780 520,830 C320,880 150,915 0,860 Z"
          fill="var(--ink-dark)"/>
    <rect class="snowflake-decor" x="940" y="560" width="112" height="160" fill="#7a6a5a" opacity="0.3"
          role="img" aria-label="Schneeflocken-Ornament"/>
    <text class="event-title" font-size="64">
      <textPath href="#titleArc" textLength="960" lengthAdjust="spacingAndGlyphs">VELVET LANTERN SERENADE</textPath>
    </text>

    <!-- special guests -->
    <g class="guest">
      <circle cx="182" cy="1058" r="133" fill="url(#violinTone)" role="img" aria-label="Violinistin mit Lasershow"/>
      <rect x="42" y="1200" width="280" height="48" fill="var(--ink-dark)"/>
      <text class="guest-label" x="182" y="1232" text-anchor="middle" font-size="19">Lena Marquardt I Violistin</text>
    </g>
    <g class="guest">
      <circle cx="520" cy="1058" r="133" fill="url(#pianistTone)" role="img" aria-label="Porträt des Pianisten"/>
      <rect x="385" y="1200" width="280" height="48" fill="var(--ink-dark)"/>
      <text class="guest-label" x="525" y="1232" text-anchor="middle" font-size="19">Tobias Renkhoff I Pianist</text>
    </g>
    <g class="guest">
      <circle cx="858" cy="1058" r="133" fill="url(#pipesTone)" role="img" aria-label="Dudelsackspieler in Highland-Uniform"/>
      <rect x="709" y="1200" width="298" height="48" fill="var(--ink-dark)"/>
      <text class="guest-label" x="858" y="1232" text-anchor="middle" font-size="19">Vechtetal Pipes &amp; Drums</text>
    </g>

    <!-- event details band -->
    <path class="info-band" d="M0,1282 C250,1268 450,1330 660,1340 C850,1350 950,1300 1052,1296 L1052,1488 L0,1488 Z"
          fill="var(--ink-dark)"/>
    <rect class="camera-decor" x="895" y="1275" width="150" height="213" fill="var(--gold)" opacity="0.85"
          role="img" aria-label="Filmkamera auf Stativ, goldene Illustration"/>
    <text class="event-date" x="58" y="1372" font-size="52">16.11. 2023, 19.30 Uhr</text>
    <text class="event-venue" x="58" y="1437" font-size="47">Bühnenhaus am Ulmenfeld in Lingen</text>
  </svg>
</main>
</body>
</html>
```